Tincture Design for Woman Owned CBD Branf

LumiVera is a luxery CBD brand for millennial women.

Our premium L Oil contains 500mg of full spectrum CBD derived from specially-sourced hemp for unparalleled purity and quality. Each dropper delivers approximately 20mg of CBD. Available in two flavors, Natural and Mint.

The goal is to design an aesthetically pleasing tincture (bottle dropper) with label and box. The final design should coincide with our brand guidelines and easily marketed for beauty consumers. We are looking for a clean design, the use of raised fonts and/or metallic is fine.

We have 4 other designs we'd like to work on with the winning designer.

Target Market(s)

Millennial Women, Income $75k+

Font styles to use
Other font styles liked:
• See Branding Sheet

Requirements
Must have
• Must follow brand guidelines (see attached for colors, font, etc)
Nice to have
• Raised font or Metallic Print

```html
<!DOCTYPE html>
<html lang="en">
<head>
<meta charset="utf-8">
<title>LumiVera CBD Oil – Label and Box</title>
<link rel="stylesheet" href="https://fonts.googleapis.com/css2?family=Josefin+Sans:wght@300;400;600&display=swap">
<style>
  :root {
    --backdrop: #f1f1ef;
    --label-white: #ffffff;
    --label-green: #1f5748;
    --copper: #c98363;
    --copper-light: #dc9c7c;
    --box-charcoal: #393735;
    --box-edge: #2c2a29;
    --soft-white: #f3ece6;
  }
  * { margin: 0; padding: 0; box-sizing: border-box; }
  html, body {
    width: 1200px;
    height: 960px;
    overflow: hidden;
    background: var(--backdrop);
    font-family: "Josefin Sans", Arial, sans-serif;
  }
  .artboard {
    position: relative;
    width: 1200px;
    height: 960px;
    display: flex;
    align-items: center;
    justify-content: center;
    gap: 140px;
  }

  /* Bottle label, flat */
  .bottle-label {
    width: 400px;
    height: 540px;
    background: var(--label-white);
    display: flex;
    flex-direction: column;
    box-shadow: 0 2px 10px rgba(0,0,0,0.06);
  }
  .label-top {
    flex: 1;
    display: flex;
    flex-direction: column;
    align-items: center;
    justify-content: center;
    padding-top: 10px;
  }
  .brand-name {
    font-weight: 400;
    letter-spacing: 0.06em;
  }
  .label-top .brand-name {
    color: var(--label-green);
    font-size: 34px;
    margin-bottom: 46px;
  }
  .label-kicker {
    color: var(--label-green);
    font-size: 20px;
    font-weight: 600;
    letter-spacing: 0.18em;
    margin-bottom: 8px;
  }
  .product-title {
    color: var(--copper);
    font-weight: 400;
    letter-spacing: 0.06em;
    line-height: 1;
  }
  .label-top .product-title { font-size: 58px; }
  .product-subtitle {
    color: var(--label-green);
    font-size: 20px;
    font-weight: 600;
    letter-spacing: 0.16em;
    margin-top: 6px;
  }
  .label-band {
    height: 170px;
    background: var(--label-green);
    display: flex;
    align-items: center;
    justify-content: center;
  }
  .spec-grid {
    width: 320px;
    border: 1.5px solid var(--copper);
    color: var(--copper-light);
    font-size: 17px;
    letter-spacing: 0.08em;
    text-align: center;
  }
  .spec-row { display: flex; }
  .spec-row + .spec-row { border-top: 1.5px solid var(--copper); }
  .spec-cell { flex: 1; padding: 12px 4px 9px; }
  .spec-cell + .spec-cell { border-left: 1.5px solid var(--copper); }
  .spec-cell.strong { font-weight: 600; flex: 0.8; }

  /* Box front, flat */
  .box-front {
    width: 330px;
    height: 800px;
    background: var(--box-charcoal);
    border: 1px solid var(--box-edge);
    display: flex;
    flex-direction: column;
    align-items: center;
    padding-top: 190px;
    box-shadow: 0 2px 14px rgba(0,0,0,0.10);
  }
  .box-front .brand-name {
    color: var(--copper-light);
    font-size: 40px;
  }
  .box-front .product-title {
    font-size: 52px;
    color: var(--copper-light);
    margin-top: 290px;
  }
  .box-front .product-subtitle {
    color: var(--soft-white);
    font-size: 19px;
    font-weight: 400;
    margin-top: 8px;
  }
  .box-flavor {
    color: var(--soft-white);
    font-size: 14px;
    letter-spacing: 0.14em;
    margin-top: 4px;
  }
  .box-volume {
    color: var(--soft-white);
    font-size: 15px;
    letter-spacing: 0.16em;
    margin-top: 74px;
  }
</style>
</head>
<body>
  <main class="artboard">
    <section class="bottle-label" aria-label="Bottle label">
      <div class="label-top">
        <div class="brand-name">LumiVera</div>
        <div class="label-kicker">PREMIUN</div>
        <h1 class="product-title">CBD OIL</h1>
        <div class="product-subtitle">FULL SPECTRUM</div>
      </div>
      <div class="label-band">
        <div class="spec-grid">
          <div class="spec-row">
            <div class="spec-cell strong">500MG</div>
            <div class="spec-cell">MINT FLAVOR</div>
          </div>
          <div class="spec-row">
            <div class="spec-cell">1 FL OZ / 30 ML</div>
          </div>
        </div>
      </div>
    </section>

    <section class="box-front" aria-label="Box front panel">
      <div class="brand-name">LumiVera</div>
      <h2 class="product-title">CBD OIL</h2>
      <div class="product-subtitle">FULL SPECTRUM</div>
      <div class="box-flavor">MINT FLAVOR</div>
      <div class="box-volume">1 FL OZ / 30 ML</div>
    </section>
  </main>
</body>
</html>
```